I need a business card representing my company, VELDRA, it's an artist management and design company. Complete name is "VELDRA Artist Mgmt. + Design Co." I need it to be world class and very appealing, sophisticated and artistically unique.
Updates

Posted an updated Brief please see. I need a business card representing my company, VELDRA, it's an artist management and design company. Complete name is "VELDRA Artist Mgmt. + Design Co." I need it to be world class and very appealing, sophisticated and artistically unique.

Designs look the same

Designs look the same

Target Market(s)

Advertisers, Entertainment Companies, Commercial companies

Industry/Entity Type

Advertising

Contact Information for Business Card

I need a business card representing my company, VELDRA, it's an artist management and design company. Complete name is "VELDRA Artist Mgmt. + Design Co." I need it to be world class and very appealing, sophisticated and artistically unique. One side can be VELDRA Artist Mgmt. + Design Co. and the other my name, Teodoro Lindqvist, my contact telephone: 412.638.2957, email veldraartist@plumora.net, my address: 3264 Harwell Ave. #517 Miami, FL 33184

Font styles to use
Other font styles liked:
• Calibri

Colors
ffffff
0455a3
f37122

Requirements
Must have
• "VELDRA" stand out bigger than the rest of the text.
Nice to have
• Name "VELDRA" can be centered on one side or in the corner or along side edges, just need something cool and different.
Should not have
• I am open just try to keep it clean looking

```html
<!DOCTYPE html>
<html lang="en">
<head>
<meta charset="UTF-8">
<title>VELDRA Business Card</title>
<link href="https://fonts.googleapis.com/css2?family=Open+Sans:wght@400;600;700&display=swap" rel="stylesheet">
<style>
  :root {
    --card-white: #ffffff;
    --brand-orange: #fe4229;
    --brand-blue: #1a68c4;
    --rule-blue: #2f78d0;
  }
  html, body {
    margin: 0;
    padding: 0;
    overflow: hidden;
    background: var(--card-white);
  }
  .card {
    position: relative;
    width: 1200px;
    height: 686px;
    background: var(--card-white);
    overflow: hidden;
    font-family: "Open Sans", Calibri, sans-serif;
  }
  .brand {
    position: absolute;
    left: 80px;
    top: 240px;
    width: 502px;
    text-align: center;
  }
  .brand-name {
    margin: 0;
    color: var(--brand-orange);
    font-weight: 600;
    font-size: 116px;
    line-height: 1;
    letter-spacing: 2px;
  }
  .brand-tagline {
    margin: 6px 0 0;
    color: var(--brand-blue);
    font-weight: 400;
    font-size: 38px;
    line-height: 1.1;
    white-space: nowrap;
  }
  .divider {
    position: absolute;
    left: 614px;
    top: 166px;
  }
  .contact {
    position: absolute;
    left: 690px;
    top: 250px;
  }
  .contact-name {
    margin: 0 0 34px;
    color: var(--brand-orange);
    font-weight: 600;
    font-size: 43px;
    line-height: 1.1;
    white-space: nowrap;
  }
  .contact-list {
    list-style: none;
    margin: 0;
    padding: 0;
  }
  .contact-item {
    display: flex;
    align-items: center;
    height: 44px;
    color: var(--brand-blue);
    font-size: 29px;
    white-space: nowrap;
  }
  .contact-icon {
    width: 26px;
    height: 26px;
    margin-right: 28px;
    flex: none;
  }
  .address-band {
    position: absolute;
    left: 0;
    bottom: 0;
    width: 1200px;
    height: 115px;
    background: var(--brand-orange);
    display: flex;
    align-items: center;
    justify-content: center;
  }
  .address {
    margin: 0;
    color: var(--card-white);
    font-weight: 700;
    font-size: 31px;
    font-style: normal;
    white-space: nowrap;
  }
</style>
</head>
<body>
<main class="card">
  <section class="brand">
    <h1 class="brand-name">VELDRA</h1>
    <p class="brand-tagline">Artist Mgmt. + Design Co.</p>
  </section>

  <svg class="divider" width="4" height="356" viewBox="0 0 4 356" aria-hidden="true">
    <defs>
      <linearGradient id="rule-fade" x1="0" y1="0" x2="0" y2="1">
        <stop offset="0" stop-color="#2f78d0" stop-opacity="0"/>
        <stop offset="0.25" stop-color="#2f78d0" stop-opacity="1"/>
        <stop offset="0.75" stop-color="#2f78d0" stop-opacity="1"/>
        <stop offset="1" stop-color="#2f78d0" stop-opacity="0"/>
      </linearGradient>
    </defs>
    <rect x="1" y="0" width="2.5" height="356" fill="url(#rule-fade)"/>
  </svg>

  <section class="contact">
    <h2 class="contact-name">Teodoro Lindqvist</h2>
    <ul class="contact-list">
      <li class="contact-item">
        <svg class="contact-icon" viewBox="0 0 26 26" aria-hidden="true">
          <rect x="1.5" y="1.5" width="23" height="23" rx="4" fill="#fff" stroke="#fe4229" stroke-width="2.5"/>
          <path d="M8.2 6.5c.6-.4 1.3-.2 1.6.4l1.2 2.3c.3.6.1 1.2-.4 1.6l-.8.6c.6 1.6 1.8 3 3.4 3.9l.7-.8c.4-.5 1.1-.6 1.6-.3l2.2 1.3c.6.3.8 1.1.4 1.6l-.9 1.3c-.5.7-1.4 1-2.2.8-4.2-1.1-7.4-4.5-8.3-8.7-.2-.8.1-1.6.8-2.1z" fill="#1a68c4"/>
          <path d="M14.5 6.5a5 5 0 0 1 5 5M14.5 9a2.5 2.5 0 0 1 2.5 2.5" fill="none" stroke="#1a68c4" stroke-width="1.4" stroke-linecap="round"/>
        </svg>
        <span>412.638.2957</span>
      </li>
      <li class="contact-item">
        <svg class="contact-icon" viewBox="0 0 26 26" aria-hidden="true">
          <rect x="1.5" y="1.5" width="23" height="23" rx="4" fill="#fff" stroke="#fe4229" stroke-width="2.5"/>
          <rect x="5.5" y="7.5" width="15" height="11" fill="#1a68c4"/>
          <path d="M5.5 7.5l7.5 6 7.5-6M5.5 18.5l5.5-5M20.5 18.5l-5.5-5" fill="none" stroke="#fff" stroke-width="1.2"/>
        </svg>
        <span>veldraartist@plumora.net</span>
      </li>
    </ul>
  </section>

  <footer class="address-band">
    <address class="address">3264 Harwell Ave. #517 Miami, FL 33184</address>
  </footer>
</main>
</body>
</html>
```